EdTech startup needs web (& logo?) redesign

LectureLoop.com is a collection of fun online tools designed to help instructors in higher education (i.e. university) build a sense of community in the classroom and enable "active learning." We have spent most of our energy on developing functionality and would love to have some real designers contribute their ideas. Everything (logos, color scheme, images, etc.) is up for grabs, but the winning design should be bootstrap friendly. We are currently using the "Broadsheet" template, but are open to others. That being said, we are less interested in getting great code than a great design. Websites we admire include quizmarbleway.com, tradenest.com, and http://layouts.fetchtrellis.com/products/application

Pages we are particularly interested in ideas for include: homepage, lucky pick, the hook, and extra tambourine. The latter three currently use images that probably can't go mainstream.

If you want to participate in the contest we would love for you to check out the site first. In order to enable this, we have set up a fictional class (PLWQ 317-4 - Beta Website Redesign). Once you create an account at www.lectureloop.com, you just enter the super-secret invite code "k9trm27x" to add yourself to the class.

Attached our some files that were used to inspire our current design. Feel free to use or ignore them as you see fit. Thanks!

Target Market(s)

college students and their instructors

Industry/Entity Type

Education

Coding

Coded - Design and coding required

Number of Pages Required

4 page

Colors
0355a3
33a6d7
cee9f5

Requirements
Must have
• cool, fun design that is boostrap friendly.
Nice to have
• I like blue, but an open to other color themes.
Should not have
• ?

```html
<!DOCTYPE html>
<html lang="en">
<head>
<meta charset="utf-8">
<title>LectureLoop</title>
<link rel="stylesheet" href="https://fonts.googleapis.com/css2?family=Oswald:wght@300;400;500&family=Roboto:wght@400;500&display=swap">
<style>
:root{
  --brand:#0355a3;
  --brand-deep:#03478a;
  --sky:#33a6d7;
  --mist:#cee9f5;
  --ink:#ffffff;
  --footer:#333333;
  --footer-text:#e8e8e8;
}
*{box-sizing:border-box;margin:0;padding:0}
html,body{width:941px;height:1200px;overflow:hidden}
body{position:relative;background:#fff;font-family:"Roboto",sans-serif;color:var(--ink)}
.abs{position:absolute}
.heading{font-family:"Oswald",sans-serif;font-weight:300}

/* header */
.site-header{left:0;top:0;width:941px;height:37px;background:var(--brand)}
.brand{left:195px;top:7px;font-family:"Oswald",sans-serif;font-weight:400;font-size:16px;color:#fff}
.main-nav{left:390px;top:0;display:flex;height:37px;font-family:"Oswald",sans-serif;font-weight:300;font-size:8.6px}
.main-nav a{color:#fff;text-decoration:none;padding:0 6px;line-height:37px}
.main-nav a.is-active{background:var(--sky);padding:0 3px}

/* hero */
.hero{left:0;top:37px;width:941px;height:246px;background:linear-gradient(100deg,#8a6a4e 0%,#c9a58a 25%,#7e93ab 55%,#b7c4cf 80%,#e5e8ea 100%)}
.hero-title{left:195px;top:157px;width:294px;height:23px;background:var(--mist);color:var(--brand);font-family:"Oswald",sans-serif;font-weight:400;font-size:13px;text-align:center;line-height:23px}
.hero-lead{left:196px;top:189px;width:287px;height:29px;background:var(--brand);font-size:9px;line-height:10.5px;text-align:center;padding-top:3px}
.pill{background:var(--brand);color:#fff;border-radius:9px;font-family:"Oswald",sans-serif;font-weight:300;font-size:8.5px;text-align:center}
.hero-btn{left:297px;top:231px;width:67px;height:16px;line-height:16px}

/* how it works */
.how{left:0;top:283px;width:941px;height:145px;background:var(--mist);overflow:hidden}
.how-panel{left:0;top:0;width:941px;height:145px}
.how-icon{left:208px;top:14px;width:128px;height:120px;background:var(--brand);border-radius:6px;opacity:.9}
.how-title{left:411px;top:8px;font-size:19px}
.rule{height:1px;background:#fff}
.rule::after{content:"";position:absolute;right:-2px;top:-1.5px;width:4px;height:4px;border-radius:50%;background:#fff}
.how-rule{left:395px;top:30px;width:118px}
.how-text{left:410px;top:47px;width:330px;font-size:8.2px;line-height:10.3px;text-align:center;color:#e9f3fb}
.how-btn{left:541px;top:114px;width:68px;height:16px;line-height:16px;background:var(--sky)}

/* programs */
.section-title{font-size:19px;color:var(--brand);text-align:center;width:941px;left:0}
.programs-title{top:440px}
.programs-rule{left:420px;top:468px;width:102px;background:var(--brand)}
.programs-rule::after{background:var(--brand)}
.program-grid{left:196px;top:479px;display:grid;grid-template-columns:repeat(4,135px);grid-auto-rows:159px;gap:4px 3.5px}
.tile{position:relative;background:linear-gradient(160deg,#2a6fb6,#0a4d97);border-bottom:5px solid var(--sky);text-align:center;overflow:hidden}
.tile svg{display:block;margin:34px auto 0;width:36px;height:36px}
.tile h3{font-family:"Oswald",sans-serif;font-weight:400;font-size:17px;margin-top:2px;letter-spacing:-.2px}
.tile.is-open{background:var(--sky);border-bottom-color:var(--sky)}
.tile.is-open .top{background:var(--brand);height:99px;padding-top:9px}
.tile.is-open svg{margin-top:0;width:34px;height:34px}
.tile.is-open p{font-size:5.8px;line-height:7.4px;padding:6px 7px 0}
.tile .pill{display:inline-block;width:68px;height:15px;line-height:15px;font-size:8.5px;margin-top:10px}

/* testimonials */
.voices{left:0;top:828px;width:941px;height:215px;background:linear-gradient(100deg,#1d5aa6,#2e6bb5 45%,#1c5aa4)}
.voices-title{top:14px;font-size:19px;color:#fff}
.voices-rule{left:408px;top:47px;width:140px}
.voices-text{left:220px;top:64px;width:501px;font-size:8.8px;line-height:10.8px;text-align:center}
.avatar{border-radius:50%;background:radial-gradient(circle at 50% 40%,#d8b8a0,#6f8fb4);border:2px solid #fff}
.av-main{left:435px;top:925px}
.voices-name{left:0;width:941px;top:169px;text-align:center;font-family:"Oswald",sans-serif;font-weight:300;font-size:10px}
.dots{left:455px;top:199px;display:flex;gap:3px}
.dots span{width:5px;height:5px;border-radius:50%;background:var(--sky)}
.dots span.on{background:#fff}

/* footer */
.site-footer{left:0;top:1043px;width:941px;height:133px;background:var(--footer)}
.col-title{font-size:14px;color:#fff}
.col-rule{width:76px;top:35px}
.sitemap{left:196px;top:42px;list-style:none;font-family:"Oswald",sans-serif;font-weight:300;font-size:7.6px;line-height:11.3px;color:var(--sky)}
.join-note{left:367px;top:43px;font-family:"Oswald",sans-serif;font-weight:400;font-size:7.4px;line-height:9.4px;color:#fff}
.email{left:367px;top:79px;width:103px;height:14px;background:#fff;border-radius:2px;font-size:5.5px;color:#999;padding:4px 4px}
.join-btn{left:366px;top:102px;width:68px;height:15px;line-height:15px}
.contact-line{left:575px;font-family:"Oswald",sans-serif;font-weight:300;font-size:7.8px;color:#fff;display:flex;align-items:center;gap:6px}
.social{left:575px;top:95px;display:flex;gap:6px}
.social span{width:21px;height:21px;border-radius:50%;background:var(--sky);font-size:5.5px;line-height:21px;text-align:center;color:#fff}
.legal{left:0;top:1176px;width:941px;height:24px;background:var(--brand);font-size:6px;line-height:24px;text-align:center}
</style>
</head>
<body>

<header class="abs site-header">
  <div class="abs brand">LectureLoop</div>
  <nav class="abs main-nav">
    <a class="is-active" href="#">Home</a>
    <a href="#">My Classes</a>
    <a href="#">Tools</a>
    <a href="#">Contact LectureLoop</a>
    <a href="#">Lucky Pick</a>
    <a href="#">The Hook</a>
    <a href="#">Extra Tambourine</a>
  </nav>
</header>

<section class="abs hero" role="img" aria-label="Photo of smiling students gathered around a laptop outdoors"></section>
<h1 class="abs hero-title">Welcome to LectureLoop!</h1>
<p class="abs hero-lead">A collection of some fun and easy-to-use tools for building classroom communities and enabling active learning</p>
<div class="abs pill hero-btn">Sing up</div>

<section class="abs how">
  <svg class="abs how-panel" viewBox="0 0 941 145" aria-hidden="true"><polygon points="396,0 941,0 941,145 345,145" fill="#0355a3"/></svg>
  <div class="abs how-icon" role="img" aria-label="Pictogram of a student working at a desk with a laptop"></div>
  <h2 class="abs heading how-title">How we works</h2>
  <div class="abs rule how-rule"></div>
  <p class="abs how-text">Lorem Ipsum is simply dummy text of the printing and typesetting industry. Lorem Ipsum has been the industry's standard dummy text ever since the 1500s, when an unknown printer took a galley of type and scrambled it to make a type specimen book. It has survived not only five centuries, but also the leap into electronic typesetting, remaining essentially unchanged</p>
  <div class="abs pill how-btn">Read More</div>
</section>

<h2 class="abs heading section-title programs-title">Our Programs</h2>
<div class="abs rule programs-rule"></div>

<div class="abs program-grid">
  <article class="tile">
    <svg viewBox="0 0 36 36" fill="none" stroke="#fff" stroke-width="2.5"><circle cx="16" cy="18" r="12"/><circle cx="16" cy="18" r="4"/></svg>
    <h3>Lucky Pick</h3>
  </article>
  <article class="tile">
    <svg viewBox="0 0 36 36"><rect x="8" y="2" width="20" height="32" rx="3" fill="#fff"/><polygon points="20,6 12,20 17,20 15,30 24,14 19,14" fill="#0a4d97"/></svg>
    <h3>Flashcards</h3>
  </article>
  <article class="tile">
    <svg viewBox="0 0 36 36" fill="none" stroke="#fff" stroke-width="2.5"><line x1="18" y1="2" x2="18" y2="14"/><path d="M18 14 C8 18 6 28 10 33 M18 14 C28 18 30 28 26 33"/></svg>
    <h3>"The Hook"</h3>
  </article>
  <article class="tile">
    <svg viewBox="0 0 36 36"><rect x="12" y="2" width="12" height="32" fill="#fff"/><rect x="16" y="7" width="4" height="5" fill="#0a4d97"/><rect x="16" y="15" width="4" height="5" fill="#0a4d97"/><rect x="16" y="23" width="4" height="5" fill="#0a4d97"/></svg>
    <h3>Virtual Clicker</h3>
  </article>
  <article class="tile">
    <svg viewBox="0 0 36 36"><path d="M13 11 V7 a5 5 0 0 1 10 0 V11" fill="none" stroke="#fff" stroke-width="2"/><path d="M6 11 H30 L32 34 H4 Z" fill="#fff"/></svg>
    <h3>Extra Tambourine</h3>
  </article>
  <article class="tile">
    <svg viewBox="0 0 36 36" fill="none" stroke="#fff" stroke-width="2"><rect x="2" y="6" width="32" height="24"/><rect x="6" y="10" width="11" height="15"/><line x1="21" y1="12" x2="30" y2="12"/><line x1="21" y1="18" x2="30" y2="18"/><line x1="21" y1="24" x2="30" y2="24"/></svg>
    <h3>Student Profiles</h3>
  </article>
  <article class="tile is-open">
    <div class="top">
      <svg viewBox="0 0 36 36" fill="none" stroke="#fff" stroke-width="3"><rect x="3" y="7" width="25" height="25"/><path d="M9 18 l6 6 L33 3"/></svg>
      <h3>Self/Peer Evals</h3>
    </div>
    <p>(coming Spring 2016) Self/Peer evaluations are a fantastic way to help students master material and deliver high quality feedback - fast. Works great in both large and small classes for either regular assignments or exams.</p>
    <span class="pill">Read More</span>
  </article>
  <article class="tile">
    <svg viewBox="0 0 36 36" fill="#fff"><rect x="2" y="4" width="32" height="28"/><g fill="#0a4d97"><rect x="6" y="8" width="4" height="4"/><rect x="13" y="8" width="4" height="4"/><rect x="20" y="8" width="4" height="4"/><rect x="27" y="8" width="4" height="4"/><rect x="6" y="16" width="4" height="4"/><rect x="13" y="16" width="4" height="4"/><rect x="20" y="16" width="4" height="4"/><rect x="27" y="16" width="4" height="4"/><rect x="6" y="24" width="4" height="4"/><rect x="13" y="24" width="4" height="4"/><rect x="20" y="24" width="4" height="4"/><rect x="27" y="24" width="4" height="4"/></g></svg>
    <h3>Rubrics</h3>
  </article>
</div>

<section class="abs voices" role="img" aria-label="Blue-tinted photo of students in a lecture hall">
  <h2 class="abs heading section-title voices-title">What are students say</h2>
  <div class="abs rule voices-rule"></div>
  <p class="abs voices-text">Lorem Ipsum is simply dummy text of the printing and typesetting industry. Lorem Ipsum has been the industry's standard dummy text ever since the 1500s, when an unknown printer took a galley of type and scrambled it to make a type</p>
  <div class="abs avatar" style="left:286px;top:136px;width:32px;height:32px" role="img" aria-label="Student portrait"></div>
  <div class="abs avatar" style="left:334px;top:136px;width:32px;height:32px" role="img" aria-label="Student portrait"></div>
  <div class="abs avatar" style="left:435px;top:97px;width:70px;height:70px" role="img" aria-label="Featured student portrait"></div>
  <div class="abs avatar" style="left:574px;top:136px;width:32px;height:32px" role="img" aria-label="Student portrait"></div>
  <div class="abs avatar" style="left:622px;top:136px;width:32px;height:32px" role="img" aria-label="Student portrait"></div>
  <div class="abs voices-name">Ben Harlow</div>
  <div class="abs dots"><span></span><span class="on"></span><span></span><span></span></div>
</section>

<footer class="abs site-footer">
  <h4 class="abs heading col-title" style="left:195px;top:14px">Site Map</h4>
  <div class="abs rule col-rule" style="left:195px"></div>
  <ul class="abs sitemap">
    <li>Home</li><li>My Classes</li><li>Tools</li><li>Contact LectureLoop</li><li>Lucky Pick</li><li>The Hook</li><li>Extra Tambourine</li>
  </ul>

  <h4 class="abs heading col-title" style="left:367px;top:14px">Join LectureLoop</h4>
  <div class="abs rule col-rule" style="left:367px;width:128px"></div>
  <p class="abs join-note">Join LectureLoop for<br>get Education</p>
  <div class="abs email">Enter Email</div>
  <div class="abs pill join-btn">Sing Up</div>

  <h4 class="abs heading col-title" style="left:575px;top:14px">Contact Us</h4>
  <div class="abs rule col-rule" style="left:575px;width:95px"></div>
  <div class="abs contact-line" style="top:44px">
    <svg width="8" height="8" viewBox="0 0 10 10"><path d="M2 0 L4 2.5 L3 4 Q4.5 6 6 7 L7.5 6 L10 8 L8.5 10 Q3 9 0 2 Z" fill="#33a6d7"/></svg>0800-555-0142</div>
  <div class="abs contact-line" style="top:65px">
    <svg width="8" height="7" viewBox="0 0 10 8"><rect width="10" height="8" fill="#33a6d7"/><path d="M0 0 L5 4.5 L10 0" stroke="#333" fill="none"/></svg>info@lectureloop.com</div>
  <div class="abs social"><span>Pal</span><span>Chirp</span><span>Nest</span></div>
</footer>

<div class="abs legal">© 2016 Lecture-loop</div>

</body>
</html>
```